Management Company Needs Web Banners

We need a new set of bidkite banners developed. Here is what we would like to have:

1. Connect the branding with tangram images from www.torvi-example.test
2. Have a "Call to Action" like a "LET'S TALK" Button

1. 728x90 Investments Need Expert Management.
2. 300x250 Senior Living Turnaround Experts
3. 728x90 TORVI Finds Lost Revenue in Senior Living Investments
4. 600x315 Senior Living Turnaround Experts

Target Market(s)

Private Equity, Health Care REITs, physicians, pharmacist, etc.

Industry/Entity Type

Management Consulting

Requirements
Must have
• A branding connection to https://www.torvi-example.test/

```html
<!DOCTYPE html>
<html lang="en">
<head>
<meta charset="utf-8">
<title>TORVI Management – Web Banner Set</title>
<link rel="stylesheet" href="https://fonts.googleapis.com/css2?family=Jost:wght@300;400;500;600&display=swap">
<style>
  :root {
    --plum-deep: #3d1a5c;
    --plum: #5e2a88;
    --violet: #9440c9;
    --violet-bright: #b556e3;
    --gold: #f6b52e;
    --ink: #2a0f3f;
    --white: #ffffff;
    --frame: #5a2a82;
    --page: #ffffff;
  }
  * { box-sizing: border-box; margin: 0; padding: 0; }
  html, body { width: 1074px; height: 1200px; overflow: hidden; background: var(--page); }
  body { font-family: "Jost", "Futura", sans-serif; }

  .stage {
    position: relative; width: 822px; height: 918px;
    transform: scale(1.3066); transform-origin: 0 0;
  }
  .banner {
    position: absolute; overflow: hidden;
    border: 1px solid var(--frame); background: var(--white);
  }
  .banner-art { position: absolute; inset: 0; }
  .art-fill-square {
    background: radial-gradient(ellipse at 50% 60%, var(--violet) 0%, var(--plum) 55%, var(--plum-deep) 100%);
  }
  .art-fill-wide {
    background: radial-gradient(ellipse at 55% 45%, var(--violet-bright) 0%, var(--violet) 45%, var(--plum) 100%);
  }
  .banner-curve { position: absolute; inset: 0; width: 100%; height: 100%; }

  .brand {
    position: absolute; display: flex; align-items: center; gap: 12px;
    color: var(--ink); font-weight: 600; letter-spacing: 0.02em; line-height: 1;
  }
  .brand-dot { border-radius: 50%; background: var(--plum); flex: none; }

  .copy { position: absolute; color: var(--white); line-height: 1; white-space: nowrap; }
  .copy-lead { font-weight: 300; display: block; }
  .copy-lead strong { font-weight: 600; }
  .copy-head {
    display: block; color: var(--gold); font-weight: 500;
    text-shadow: 1px 1px 2px rgba(40, 10, 60, 0.5);
  }
  .copy-center { left: 0; right: 0; text-align: center; }

  .cta {
    position: absolute; display: flex; align-items: center; justify-content: center;
    border: 2px solid var(--white); color: var(--white);
    font-weight: 400; letter-spacing: 0.02em;
  }

  /* 300x250 */
  .b-medium { left: 259px; top: 44px; width: 300px; height: 250px; }
  .b-medium .brand { left: 0; right: 0; justify-content: center; top: 14px; font-size: 42px; }
  .b-medium .brand-dot { width: 52px; height: 52px; }
  .b-medium .copy { top: 128px; }
  .b-medium .copy-lead { font-size: 22px; }
  .b-medium .copy-head { font-size: 24px; margin-top: 8px; }
  .b-medium .cta { left: 102px; top: 199px; width: 95px; height: 35px; font-size: 13px; }

  /* 728x90 */
  .b-leader-a { left: 47px; top: 324px; width: 728px; height: 90px; }
  .b-leader-b { left: 47px; top: 442px; width: 728px; height: 90px; }
  .b-leader-a .brand, .b-leader-b .brand { left: 22px; top: 15px; font-size: 38px; }
  .b-leader-a .brand-dot, .b-leader-b .brand-dot { width: 58px; height: 58px; }
  .b-leader-a .copy { left: 287px; top: 17px; }
  .b-leader-a .copy-lead { font-size: 22px; }
  .b-leader-a .copy-head { font-size: 28px; margin-top: 4px; }
  .b-leader-b .copy { left: 285px; top: 16px; }
  .b-leader-b .copy-lead { font-size: 19px; }
  .b-leader-b .copy-head { font-size: 29px; margin-top: 5px; }
  .b-leader-a .cta, .b-leader-b .cta { left: 603px; top: 26px; width: 105px; height: 40px; font-size: 14px; }

  /* 600x315 */
  .b-social { left: 111px; top: 562px; width: 600px; height: 315px; }
  .b-social .brand { left: 0; right: 0; justify-content: center; top: 22px; font-size: 52px; gap: 16px; }
  .b-social .brand-dot { width: 72px; height: 72px; }
  .b-social .copy { top: 162px; }
  .b-social .copy-lead { font-size: 34px; }
  .b-social .copy-head { font-size: 39px; margin-top: 8px; }
  .b-social .cta { left: 241px; top: 255px; width: 117px; height: 44px; font-size: 16px; }
</style>
</head>
<body>
<main class="stage">

  <section class="banner b-medium" aria-label="300 by 250 banner">
    <div class="banner-art art-fill-square" role="img" aria-label="Purple tangram-shape background"></div>
    <svg class="banner-curve" viewBox="0 0 300 250" preserveAspectRatio="none" aria-hidden="true">
      <path d="M0 0 H300 V72 Q150 140 0 72 Z" fill="#fff"/>
    </svg>
    <div class="brand"><span class="brand-dot"></span>TORVI</div>
    <p class="copy copy-center">
      <span class="copy-lead">Senior Living</span>
      <span class="copy-head">TURNAROUND EXPERTS</span>
    </p>
    <span class="cta">LET’S TALK</span>
  </section>

  <section class="banner b-leader-a" aria-label="728 by 90 banner">
    <div class="banner-art art-fill-wide" role="img" aria-label="Purple tangram-shape background"></div>
    <svg class="banner-curve" viewBox="0 0 728 90" preserveAspectRatio="none" aria-hidden="true">
      <path d="M0 0 H268 Q246 60 222 90 H0 Z" fill="#fff"/>
    </svg>
    <div class="brand"><span class="brand-dot"></span>TORVI</div>
    <p class="copy">
      <span class="copy-lead">Investments Need</span>
      <span class="copy-head">EXPERT MANAGEMENT.</span>
    </p>
    <span class="cta">LET’S TALK</span>
  </section>

  <section class="banner b-leader-b" aria-label="728 by 90 banner">
    <div class="banner-art art-fill-wide" role="img" aria-label="Purple tangram-shape background"></div>
    <svg class="banner-curve" viewBox="0 0 728 90" preserveAspectRatio="none" aria-hidden="true">
      <path d="M0 0 H268 Q246 60 222 90 H0 Z" fill="#fff"/>
    </svg>
    <div class="brand"><span class="brand-dot"></span>TORVI</div>
    <p class="copy">
      <span class="copy-lead"><strong>TORVI</strong> Finds Lost Revenue in Senior</span>
      <span class="copy-head">LIVING INVESTMENTS</span>
    </p>
    <span class="cta">LET’S TALK</span>
  </section>

  <section class="banner b-social" aria-label="600 by 315 banner">
    <div class="banner-art art-fill-square" role="img" aria-label="Purple tangram-shape background"></div>
    <svg class="banner-curve" viewBox="0 0 600 315" preserveAspectRatio="none" aria-hidden="true">
      <path d="M0 0 H600 V92 Q300 185 0 92 Z" fill="#fff"/>
    </svg>
    <div class="brand"><span class="brand-dot"></span>TORVI</div>
    <p class="copy copy-center">
      <span class="copy-lead">Senior Living</span>
      <span class="copy-head">TURNAROUND EXPERTS</span>
    </p>
    <span class="cta">LET’S TALK</span>
  </section>

</main>
</body>
</html>
```